Flyer für Onlineshop
Zielgruppe
Wir vertreiben 2 Komponentenlacke, wasserbasiert, auf Polyurethanharz Basis zur Sanierung von Fliesen vieles und mehr.
Aufgabenstellung
Wir möchten eine Fleyer speziell für die Fliesenfarben.
Das Design soll frisch, modern und ansprechend gestaltet sein. Wir möchten den Fleyer öffentlich auslegen aber auch an z.B Jugendherbergen, Kurhäuser ect. und privat Personen verteilen um darauf aufmerksam zu machen das es eine güstige alternative zum Neukauf gibt.
Auf dem Flyer soll in der Fliesenlack im Vordergrund stehen es darf aber kurz auf weitere Produkte aufmerksam gemacht werden.
für die Größe des Flyers habe ich keine genauen Vorstellungen lasse mich überraschen.
Sie finden die Informationen die Sie benötigen unter
www.tumar-lackwerk.com/farben-lacke/fliesenfarbe
Der Fleyer sollte die Maße DIN lang (105 x 210 mm) hoch / 4 Seiten
Aber auch andere Vorschläge sind Willkommen
Also Logo habe ich verschiedene jpg´s hochgeladen..leider ist die qualität nicht sehr gut aber vielleicht können Sie was damit anfangen.
Bei weiteren Fragen stehe ich Ihnen gerne zur Verfügung

```html
<!DOCTYPE html>
<html lang="de">
<head>
<meta charset="utf-8">
<title>Fliesenfarbe – Flyer DIN lang</title>
<link rel="stylesheet" href="https://fonts.googleapis.com/css2?family=Oswald:wght@500;600&family=Open+Sans:wght@400;700&display=swap">
<style>
  :root {
    --stage: #d9d9d9;
    --paper: #ffffff;
    --inner: #f2f2f2;
    --brand-blue: #1f5fa8;
    --ink: #1e1e1e;
    --muted: #4a4a4a;
  }
  * { box-sizing: border-box; margin: 0; padding: 0; }
  html, body { width: 1200px; height: 899px; overflow: hidden; }
  body {
    background: radial-gradient(circle at 50% 40%, #ececec 0%, var(--stage) 75%);
    font-family: "Open Sans", Arial, sans-serif;
    color: var(--ink);
    position: relative;
  }
  .spread {
    position: absolute; left: 250px; top: 95px;
    width: 700px; height: 700px;
    display: flex;
    box-shadow: 0 18px 40px rgba(0,0,0,.22);
  }
  .page {
    width: 350px; height: 700px;
    background: var(--paper);
    position: relative; overflow: hidden;
    display: flex; flex-direction: column;
  }
  .page--right { background: var(--inner); border-left: 1px solid #d4d4d4; }

  .headline {
    font-family: "Oswald", "Arial Narrow", sans-serif;
    font-weight: 600; text-transform: uppercase;
    letter-spacing: 2px; color: var(--brand-blue);
    display: flex; align-items: center; gap: 8px;
  }
  .headline__mark { width: 16px; height: 24px; background: var(--brand-blue); flex: none; }
  .subline { font-size: 9.5px; font-weight: 700; color: var(--muted); }
  .copy { font-size: 10.5px; line-height: 1.55; text-align: justify; }
  .copy b { font-weight: 700; }

  /* left page */
  .page--left { padding: 34px 24px 0 24px; }
  .page--left .headline { font-size: 28px; }
  .page--left .subline { margin: 4px 0 12px 24px; }
  .tile-photo-row { display: flex; margin: 14px -24px 16px -24px; height: 150px; }
  .tile-photo-row__band { width: 44px; background: var(--brand-blue); margin-top: 0; height: 70px; }
  .tile-photo {
    flex: 1;
    background: linear-gradient(125deg, #c9b39a 0%, #a9532c 35%, #e3d5c0 55%, #8c4a2a 78%, #d7c2a6 100%);
  }

  /* right page */
  .page--right { padding: 0 0 22px 0; }
  .bath-top-row { display: flex; margin-top: 22px; height: 118px; }
  .bath-top-row__band { width: 28px; background: var(--brand-blue); align-self: flex-end; height: 58px; }
  .bath-photo-top {
    flex: 1; margin-right: 24px;
    background: linear-gradient(160deg, #6fb6de 0%, #cfe9f6 45%, #3b8fc4 100%);
  }
  .right-body { padding: 14px 24px 0 28px; }
  .page--right .headline { font-size: 17px; gap: 0; }
  .page--right .subline { margin: 2px 0 10px; }
  .features { display: flex; gap: 8px; margin-bottom: 14px; }
  .features__mark { width: 14px; height: 42px; background: var(--brand-blue); flex: none; }
  .features ul { list-style: none; font-size: 9.5px; line-height: 1.5; color: var(--muted); }
  .web { font-weight: 700; }
  .bath-bottom-row { display: flex; margin-top: auto; height: 150px; padding-left: 24px; }
  .bath-photo-bottom {
    flex: 1;
    background: linear-gradient(120deg, #8a6c52 0%, #d8c5ad 45%, #f3ece2 70%, #b08d6c 100%);
  }
  .bath-bottom-row__band { width: 26px; background: var(--brand-blue); height: 120px; align-self: center; }
</style>
</head>
<body>
  <main class="spread">
    <section class="page page--left">
      <h1 class="headline"><span class="headline__mark"></span>Die Fliesenfarbe</h1>
      <p class="subline">Die günstige Alternative zum Neukauf Ihrer Fliesen</p>
      <p class="copy">Sie haben alte Fliesen und möchten Ihr Badezimmer erneuern, ohne gleich alles neu zu kaufen? Mit unserer Fliesenfarbe gelingt die Sanierung schnell, sauber und günstig. Der wasserbasierte Lack auf Polyurethanharz-Basis haftet dauerhaft und bleibt <b>pflegeleicht und strapazierfähig.</b></p>
      <div class="tile-photo-row">
        <div class="tile-photo-row__band"></div>
        <div class="tile-photo" role="img" aria-label="Foto: Fliesenmuster in Terrakotta- und Sandtönen"></div>
      </div>
      <p class="copy">Ob in <b>Bad, Küche oder Laden</b> – mit dem 2-Komponentenlack streichen Sie Ihre Fliesen direkt über. Die Fugen werden mitlackiert und erhalten so einen <b>einheitlichen Look.</b> Die Farbe ist abriebfest, wasserfest und beständig gegen Reinigungsmittel. So entsteht ein neuer Raum ohne Staub, Lärm und teure Handwerker. Auch <b>Jugendherbergen, Kurhäuser und Ferienwohnungen</b> sparen damit Zeit und Kosten. Einfach auftragen, trocknen lassen und fertig – eine echte Alternative zum Neukauf, die sich <b>sofort lohnt.</b></p>
    </section>

    <section class="page page--right">
      <div class="bath-top-row">
        <div class="bath-top-row__band"></div>
        <div class="bath-photo-top" role="img" aria-label="Foto: helles Badezimmer mit blauen Fliesen"></div>
      </div>
      <div class="right-body">
        <h2 class="headline">Gebrauchsfertige Fliesenfarben</h2>
        <p class="subline">in vielen schönen Farbvariationen</p>
        <div class="features">
          <span class="features__mark"></span>
          <ul>
            <li>wasserverdünnbar für ein ganzes Badezimmer</li>
            <li>auch für Keller oder Garage</li>
            <li>hochglänzend für Bad oder Küche</li>
          </ul>
        </div>
        <p class="copy">Dabei stehen Ihnen <b>zahlreiche Farbtöne</b> zur Auswahl, damit für jeden Möbelstil und jeden Geschmack das Passende gefunden werden kann. Neben <b>hellen und dunklen</b> Varianten sind <b>kalte und warme Töne</b> verfügbar. Bevor der Decklack aufgetragen werden kann, sind eine entsprechende Vorbehandlung, das Trocknen und der Auftrag der Grundierung nötig. Die dafür nötigen Produkte können auch separat <b>in unserem Onlineshop</b> erworben werden. Wir beraten Sie gerne! Besuchen Sie uns einfach auf <span class="web">www.tumar-lackwerk.com</span></p>
      </div>
      <div class="bath-bottom-row">
        <div class="bath-photo-bottom" role="img" aria-label="Foto: modernes Bad mit Holzwaschtisch und Glasdusche"></div>
        <div class="bath-bottom-row__band"></div>
      </div>
    </section>
  </main>
</body>
</html>
```